Etiketten für Nahrungsergänzung für Tiere
Zielgruppe
Wir stellen kolloidale Mischungen für Tiere her. Dies sind grob gesagt Nahrungsmittelergänzungen. Die Zielgruppe sind Tierbesitzer bzw. gesundheitsbewusste Menschen.
Aufgabenstellung
natürlich, in braun, beige, gold oder hellblau Tönen. Das Etikett wird auf eine Flasche aufgebraucht in der sich eine Flüssigkeit befindet. Das Etikett ist breiter als hoch. 115 x 61 mm (B x H)
Bisher haben wir blaue Flaschen verwendet und waren dadurch mit der Farbgebung ehr kühl und reduziert. In Zukunft wollen wir braune Flaschen mit schwarzen Deckel verwendet. Damit darf die Farbgebung auch wärmer, natürlich und das Etikett auch mit mehr Details versehen werden.
In den Uploads füge ich das aktuell Logo hinzu. Dies verwenden wir in braun/gold und in grün. Falls sich diese Gestaltung nicht so günstig auswirkt, haben wir ein 'alternative' Logo hinzugefügt. Da die Seite nächstes Jahr komplett überarbeitet wird und unsere Firma sich vergrößert, kann diese Änderung durchgeführt werden.
Ich lade noch ein Etikett hoch, welches wir für die Einzelelemente nutzen. Hier sind und bleiben die Flaschen nach wir vor blau (Herstellervorgaben), dadurch sind die Etikett sehr kühl und reduziert. Das darf auf den Entwurf für die Mischungen sehr gern deutlich verändert werden :-)

```html
<!DOCTYPE html>
<html lang="de">
<head>
<meta charset="utf-8">
<title>Ionic Etiketten</title>
<link rel="stylesheet" href="https://fonts.googleapis.com/css2?family=Figtree:wght@400;500;700;800&display=swap">
<style>
  :root{
    --page:#f1f1f1;
    --cream:#f6f5e0;
    --ring:#e2d9c3;
    --brown:#5c4033;
    --brown-edge:#a87c5a;
    --sky:#a8dbdd;
    --sky-edge:#d5edf0;
    --ink:#3a2a22;
    --ink-dark:#2a2a2a;
    --box:#ffffff;
  }
  *{box-sizing:border-box;margin:0;padding:0}
  html,body{width:1200px;height:1199px;overflow:hidden;background:var(--page);font-family:"Figtree",sans-serif}
  .label{position:absolute;left:250px;width:700px;height:372px;background:var(--cream);overflow:hidden;box-shadow:4px 10px 14px rgba(0,0,0,.22)}
  .label--titan{top:180px;--accent:var(--brown);--edge:var(--brown-edge);--title:var(--brown);--pilltext:#f6f5e0;--brandtext:var(--cream)}
  .label--silizium{top:648px;--accent:var(--sky);--edge:var(--sky-edge);--title:var(--ink-dark);--pilltext:var(--ink);--brandtext:var(--ink-dark)}
  .stripe{position:absolute;left:0;right:0;height:6px;background:var(--edge);z-index:2}
  .stripe--top{top:0}.stripe--bottom{bottom:0}
  .texture{position:absolute;border-radius:50%;background:radial-gradient(circle,var(--ring) 0%,rgba(226,217,195,.55) 45%,rgba(226,217,195,0) 70%)}
  .texture--top{right:-80px;top:-70px;width:200px;height:200px}
  .texture--bottom{left:-110px;top:232px;width:240px;height:240px}
  .tab{position:absolute;left:68px;top:0;width:230px;height:274px;background:var(--accent);border:5px solid var(--edge);border-top:none;border-radius:0 0 115px 115px;display:flex;flex-direction:column;align-items:center;padding-top:118px;gap:10px;z-index:1}
  .brand-dot{width:14px;height:14px;border-radius:50%;background:var(--brandtext)}
  .brand-name{color:var(--brandtext);font-weight:700;font-size:22px;letter-spacing:.04em}
  .title{position:absolute;left:96px;top:296px;font-size:29px;font-weight:400;color:var(--title);letter-spacing:-.01em}
  .title b{font-weight:800}
  .info{position:absolute;left:351px;top:46px;width:290px;font-size:10.4px;line-height:1.4;color:var(--ink)}
  .info p{margin-bottom:12px}
  .info .justify{text-align:justify;margin-bottom:8px}
  .info .maker{font-weight:700}
  .sizes{position:absolute;left:346px;right:0;top:264px;height:31px;background:var(--accent);border-radius:16px 0 0 16px;display:flex;align-items:center;gap:18px;padding-left:14px;font-size:10.4px;color:var(--pilltext)}
  .size{display:flex;align-items:center;gap:6px}
  .size::before{content:"";width:11px;height:11px;background:var(--box);border:1px solid #8a8a8a}
  .batch{position:absolute;left:351px;top:321px;font-size:10.4px;font-weight:700;color:var(--ink)}
</style>
</head>
<body>
  <section class="label label--titan">
    <div class="stripe stripe--top"></div>
    <div class="stripe stripe--bottom"></div>
    <div class="texture texture--top" role="img" aria-label="Dekoratives Ringmuster in Beige"></div>
    <div class="texture texture--bottom" role="img" aria-label="Dekoratives Ringmuster in Beige"></div>
    <div class="tab"><span class="brand-dot"></span><span class="brand-name">Quellgrund</span></div>
    <h2 class="title">IONIC <b>TITAN</b></h2>
    <div class="info">
      <p>Kolloid in wässriger Lösung<br>Inhaltsstoffe: 99,9% reines Titan in Bidestillat</p>
      <p>Kolloid aus Protonenresonanzverfahren<br>50 ppm bei Herstellung in doppelt destilliertem Wasser</p>
      <p class="justify">Bei Raumtemperatur und lichtgeschützt lagern. Vor Mikrowellen und magnetischen Feldern fernhalten. PPM-Messmethode: Atomspektralanalyse. Anwendung nach dem Quantenprinzip der verschränkten Teilchen. Nicht für den menschlichen Verzehr geeignet.</p>
      <p class="maker">Quellgrund, Am Lindenhang 8, 07318 Eichwalde</p>
    </div>
    <div class="sizes"><span class="size">30 ml</span><span class="size">50 ml</span><span class="size">100 ml</span><span class="size">200 ml</span></div>
    <div class="batch">MHD=Chargen-Nr:</div>
  </section>

  <section class="label label--silizium">
    <div class="stripe stripe--top"></div>
    <div class="stripe stripe--bottom"></div>
    <div class="texture texture--top" role="img" aria-label="Dekoratives Ringmuster in Beige"></div>
    <div class="texture texture--bottom" role="img" aria-label="Dekoratives Ringmuster in Beige"></div>
    <div class="tab"><span class="brand-dot"></span><span class="brand-name">Quellgrund</span></div>
    <h2 class="title">IONIC <b>SILIZIUM</b></h2>
    <div class="info">
      <p>Kolloid in wässriger Lösung<br>Inhaltsstoffe: 99,999% reines Titan in Bidestillat</p>
      <p>Kolloid aus Protonenresonanzverfahren<br>55 ppm bei Herstellung in doppelt destilliertem Wasser</p>
      <p class="justify">Bei Raumtemperatur und lichtgeschützt lagern. Vor Mikrowellen und magnetischen Feldern fernhalten. PPM-Messmethode: Atomspektralanalyse. Anwendung nach dem Quantenprinzip der verschränkten Teilchen. Nicht für den menschlichen Verzehr geeignet.</p>
      <p class="maker">Miriam Albrecht, Am Lindenhang 8, 07318 Eichwalde</p>
    </div>
    <div class="sizes"><span class="size">30 ml</span><span class="size">50 ml</span><span class="size">100 ml</span><span class="size">200 ml</span></div>
    <div class="batch">MHD=Chargen-Nr:</div>
  </section>
</body>
</html>
```